Business Consultants - Require an A4 size presentation folder with inserts for a new exciting Standa

We have developed a service/product where we help small and medium businesses to draft up their policies & procedures manual for their business. This manual has everything in it on how to run their business. From how to answer the phone, to how to process invoices, through to HR information, and marketing plans.

We need a professional but modern looking presentation folder to house all this information. The size will be A4. Inside we will have up to 12 inserts to seperate the different chapters/topic. For example. Sales, Marketing, Administration, Operations, Finance.

Each folder will be branded with the client logo and name on the front, hence it does need to be relativity simple and neutral as to not clash with their colours etc.

We will have our Logo and contact details on the back of the folder.

The design aspect may well come for the chapter inserts. Again the actual tabs will need to be neutral so that we can write on them so that when you open the front cover you can quickly go the chapter you need.

Be warned I do not want any generic design gallery type designs. They stand out as cheap and nasty. I need you actually put some thought into these !!!

Attached is our Logo, and a two photos of the sort of shape and size of the anticipated folders.
Updates

Target Market(s)

Small & Medium Brick & Mortar Business Owners

Industry/Entity Type

Business Consultant

Colors

Designer to choose colors to be used in the design.

Requirements
Must have
• Must be clean, crisp, but with some cool simple design elements
Should not have
• Too many bold colours as it will clash with our client logos, which we have no control over what colour they are

```html
<!DOCTYPE html>
<html lang="en">
<head>
<meta charset="utf-8">
<title>Presentation Folder – Chapter Tabs</title>
<link rel="stylesheet" href="https://fonts.googleapis.com/css2?family=Didact+Gothic&display=swap">
<style>
  :root {
    --page: #ffffff;
    --folder-edge: #3a3a3a;
    --panel-dark: #58585a;
    --text-grey: #555557;
    --text-light: #ffffff;
    --tab-frame: #ffffff;
    --tab-sales: #62c9cf;
    --tab-marketing: #221f4f;
    --tab-administration: #7b78b9;
    --tab-operations: #6f9895;
    --tab-finance: #c9d4d9;
  }
  html, body {
    margin: 0;
    padding: 0;
    width: 1200px;
    height: 1000px;
    overflow: hidden;
    background: var(--page);
  }
  .canvas {
    position: relative;
    width: 1200px;
    height: 1000px;
    font-family: "Didact Gothic", "Century Gothic", sans-serif;
  }
  .folder {
    position: absolute;
    left: 298px;
    top: 62px;
    width: 604px;
    height: 877px;
    border: 1.5px solid var(--folder-edge);
    box-sizing: border-box;
    background: var(--page);
    overflow: hidden;
  }
  .folder__spine-panel {
    position: absolute;
    left: 225px;
    top: 0;
    right: 0;
    bottom: 0;
    background: var(--panel-dark);
  }
  .folder__client-logo {
    position: absolute;
    left: 46px;
    top: 58px;
    margin: 0;
    font-size: 34px;
    font-weight: 400;
    letter-spacing: 2px;
    line-height: 1.2;
    color: var(--text-grey);
  }
  .chapter-tab {
    position: absolute;
    left: 195px;
    width: 400px;
    height: 72px;
    display: flex;
    align-items: center;
  }
  .chapter-tab__swatch {
    width: 63px;
    height: 64px;
    border: 4px solid var(--tab-frame);
    border-left: none;
    flex: none;
  }
  .chapter-tab__label {
    margin-left: 18px;
    font-size: 34px;
    letter-spacing: 1.6px;
    color: var(--text-light);
  }
  .chapter-tab--sales { top: 173px; }
  .chapter-tab--marketing { top: 317px; }
  .chapter-tab--administration { top: 461px; }
  .chapter-tab--operations { top: 605px; }
  .chapter-tab--finance { top: 749px; }
  .chapter-tab--sales .chapter-tab__swatch { background: var(--tab-sales); }
  .chapter-tab--marketing .chapter-tab__swatch { background: var(--tab-marketing); }
  .chapter-tab--administration .chapter-tab__swatch { background: var(--tab-administration); }
  .chapter-tab--operations .chapter-tab__swatch { background: var(--tab-operations); }
  .chapter-tab--finance .chapter-tab__swatch { background: var(--tab-finance); }
  .brand-name {
    position: absolute;
    left: 14px;
    top: 802px;
    width: 160px;
    text-align: center;
    font-size: 13px;
    letter-spacing: 0.2px;
    color: var(--text-grey);
    white-space: nowrap;
  }
</style>
</head>
<body>
  <main class="canvas">
    <section class="folder">
      <div class="folder__spine-panel"></div>
      <h1 class="folder__client-logo">Logo</h1>

      <div class="chapter-tab chapter-tab--sales">
        <span class="chapter-tab__swatch"></span>
        <span class="chapter-tab__label">Sales</span>
      </div>
      <div class="chapter-tab chapter-tab--marketing">
        <span class="chapter-tab__swatch"></span>
        <span class="chapter-tab__label">Marketing</span>
      </div>
      <div class="chapter-tab chapter-tab--administration">
        <span class="chapter-tab__swatch"></span>
        <span class="chapter-tab__label">Administration</span>
      </div>
      <div class="chapter-tab chapter-tab--operations">
        <span class="chapter-tab__swatch"></span>
        <span class="chapter-tab__label">Operations</span>
      </div>
      <div class="chapter-tab chapter-tab--finance">
        <span class="chapter-tab__swatch"></span>
        <span class="chapter-tab__label">Finance</span>
      </div>

      <div class="brand-name">NORTHFIELD ADVISORY</div>
    </section>
  </main>
</body>
</html>
```